New Organic Medical Marijuana Packging Design

New Organic Grower needs a fresh new design for the retail package.
the idea is to incorporate a compostable materials and come up with the resealable pouch/baggy that can hold the medicine and maybe another compartment for the promotional material (like rolling papers).
Company name is Bram's Organic. (bram- Bramwell is the name of our guru grower who also spends a ton of time playing in the dirt).
Medicine will need to be visible (whole or partially )through the side of the pack. an idea attached..

```html
<!DOCTYPE html>
<html lang="en">
<head>
<meta charset="utf-8">
<title>Bram's Organic – Medical Cannabis Label</title>
<link rel="stylesheet" href="https://fonts.googleapis.com/css2?family=Questrial&display=swap">
<style>
  :root {
    --kraft: #c8ab8a;
    --kraft-light: #d2b797;
    --kraft-dark: #bb9c7a;
    --ink: #3b3a38;
    --rule: #4a4744;
    --leaf: #2f6b2a;
    --leaf-light: #4c8b3a;
    --icon-grey: #58585a;
  }
  html, body {
    margin: 0;
    padding: 0;
    overflow: hidden;
  }
  body {
    width: 764px;
    height: 1200px;
  }
  .label {
    position: relative;
    width: 764px;
    height: 1200px;
    overflow: hidden;
    background: radial-gradient(ellipse at 60% 40%, var(--kraft-light), var(--kraft) 55%, var(--kraft-dark));
    font-family: "Questrial", "Century Gothic", sans-serif;
    color: var(--ink);
  }
  .label p, .label h1, .label h2 {
    margin: 0;
    font-weight: 400;
  }
  .leaf-artwork {
    position: absolute;
    left: -60px;
    top: -80px;
    width: 620px;
    height: 610px;
    border-radius: 0 0 62% 38% / 0 0 48% 70%;
    background: radial-gradient(ellipse at 10% 40%, var(--leaf-light), var(--leaf) 70%);
    opacity: 0.92;
  }
  .maker-line {
    position: absolute;
    top: 533px;
    left: 0;
    width: 764px;
    text-align: center;
    font-size: 23px;
    letter-spacing: 6px;
  }
  .rule {
    position: absolute;
    height: 0;
    border-top: 1.5px solid var(--rule);
  }
  .rule--brand-top { top: 585px; left: 65px; width: 630px; }
  .rule--brand-bottom-a { top: 718px; left: 65px; width: 630px; }
  .rule--brand-bottom-b { top: 723px; left: 65px; width: 630px; }
  .rule--weight-top { top: 943px; left: 0; width: 764px; }
  .rule--weight-bottom { top: 1016px; left: 0; width: 764px; }
  .brand-name {
    position: absolute;
    top: 606px;
    left: 65px;
    width: 630px;
    text-align: center;
    font-size: 72px;
    letter-spacing: 2px;
    line-height: 1;
  }
  .product-name {
    position: absolute;
    top: 805px;
    left: 0;
    width: 764px;
    text-align: center;
    font-size: 46px;
    letter-spacing: 8px;
  }
  .net-weight {
    position: absolute;
    top: 958px;
    left: 0;
    width: 764px;
    text-align: center;
    font-size: 33px;
    letter-spacing: 8px;
  }
  .label .net-weight { font-weight: 700; }
  .warning-mark {
    position: absolute;
    top: 1047px;
    left: 95px;
    width: 80px;
    height: 80px;
    background: var(--icon-grey);
  }
  .warning-title {
    position: absolute;
    top: 1044px;
    left: 203px;
    font-size: 46px;
    letter-spacing: 6.5px;
    line-height: 1;
  }
  .warning-note {
    position: absolute;
    top: 1100px;
    left: 203px;
    font-size: 30px;
    letter-spacing: 7.5px;
    line-height: 1;
  }
</style>
</head>
<body>
  <main class="label">
    <div class="leaf-artwork" role="img" aria-label="Photograph of a green cannabis leaf fanning in from the top-left corner"></div>

    <p class="maker-line">An organic product by</p>
    <div class="rule rule--brand-top"></div>
    <h1 class="brand-name">Bram's Organic</h1>
    <div class="rule rule--brand-bottom-a"></div>
    <div class="rule rule--brand-bottom-b"></div>

    <h2 class="product-name">Medical Cannabis</h2>

    <div class="rule rule--weight-top"></div>
    <p class="net-weight">net wt. 50gms</p>
    <div class="rule rule--weight-bottom"></div>

    <div class="warning-mark" aria-hidden="true"></div>
    <p class="warning-title">WARNING</p>
    <p class="warning-note">FOR MEDICL USE ONLY</p>
  </main>
</body>
</html>
```